Center for Cellular Datacraft wordpress design

We need a wordpress design for the new Center for Cellular Datacraft at the Halvorsen State College. We are a research institute focused on medical and biological research involving big data and informatics. The website has to be eyecatching and appropriate for an academic context, with easily updated content.

Press release here: http://www.hscmed.halvorsen.edu/news/News_Releases/2013/02/cellular/

We would prefer to use images from our research labs over stock art, but feel free to use placeholders for now. Please contact me if there are specific types of images you need.

Target Market(s)

Tech-savvy academics, faculty, students, general laypeople

Industry/Entity Type

Medical

Requirements
Must have
• Use existing logo (attached, other versions available upon request)

Sections for:
Mission statement (draft version attached)
Educational Programs: there is only one at the moment, but we will need the option to add more
Faculty members/resident staff (contact database); webform to apply to join
Events calendar/list
Emphasis on search engine optimization
Nice to have
• News/publication tabs for the front page (similar to those on http://www.trelvo.halvorsen.edu/)

It would be helpful if you could use the Halvorsen color palette: http://www.halvorsen.edu/webservices/styleguide/color.html

```html
<!DOCTYPE html>
<html lang="en">
<head>
<meta charset="utf-8">
<title>About Us 2 – Center for Cellular Datacraft</title>
<link rel="stylesheet" href="https://fonts.googleapis.com/css2?family=PT+Sans:wght@400;700&family=Libre+Baskerville:ital@1&family=Arimo:wght@400;700&display=swap">
<style>
:root{
  --ink:#222;
  --body:#444;
  --muted:#777;
  --line:#e3e3e3;
  --band:#f3f3f3;
  --topbar:#f7f7f7;
  --accent:#c8102e;
  --brand:#1a2f6b;
  --footer:#2e2e2e;
  --footer-line:#474747;
  --footer-text:#d6d6d6;
  --base:#111;
  --cal-head:#444;
  --cal-cell:#e9e9e9;
  --cal-off:#d9d9d9;
  --today:#4aa3c9;
}
*{box-sizing:border-box;margin:0;padding:0}
html,body{width:885px;height:1200px;overflow:hidden;background:#fff}
body{position:relative;font-family:"PT Sans",sans-serif;color:var(--body)}
.abs{position:absolute}
ul{list-style:none}

.top-bar{left:0;top:0;width:885px;height:18px;background:var(--topbar)}
.top-bar a{position:absolute;right:62px;top:6px;font:7px "Arimo",sans-serif;color:var(--muted);text-decoration:none}

.brand{left:56px;top:28px;display:flex;align-items:center;gap:9px}
.brand-mark{width:30px;height:30px;background:var(--brand)}
.brand-name{font:700 18px/19px "PT Sans",sans-serif;color:var(--brand);width:210px}

.main-nav{top:42px;right:76px;display:flex;gap:8px;font:8.5px "Arimo",sans-serif}
.main-nav a{color:var(--muted);text-decoration:none;position:relative}
.main-nav a.current{color:var(--ink)}
.main-nav a.current::after{content:"";position:absolute;left:0;right:0;top:16px;height:2px;background:var(--accent)}

.title-band{left:6px;top:97px;width:873px;height:93px;background:var(--band);text-align:center;border-top:1px solid #e6e6e6}
.title-band h1{font:400 18px "PT Sans",sans-serif;color:var(--ink);margin-top:24px}
.title-band p{font-size:11.5px;color:var(--ink);margin-top:10px}

.hero{left:63px;top:227px;width:487px;height:238px;background:linear-gradient(90deg,#7f8ea8 0%,#c3cbd6 45%,#dfe4ea 100%)}
.hero blockquote{position:absolute;right:30px;top:38px;width:260px;text-align:right;font:italic 21px/26px "Libre Baskerville",serif;color:#333}
.hero cite{position:absolute;right:32px;top:122px;font:normal 8px "Arimo",sans-serif;color:#444}

.article{left:62px;top:493px;width:502px;font-size:8.6px;line-height:15.7px;color:var(--body)}
.article p+p{margin-top:5px}

.section-title{font:400 11px "PT Sans",sans-serif;color:var(--ink);display:inline-block;padding-bottom:4px;border-bottom:1px solid var(--ink)}

.more{left:63px;top:682px;width:372px}
.accordion{margin-top:12px}
.acc-item{border:1px solid var(--line);margin-bottom:5px;padding:0 10px;font-size:8.6px}
.acc-head{height:27px;display:flex;justify-content:space-between;align-items:center;color:var(--muted)}
.acc-head b{font-size:11px;color:var(--ink)}
.acc-item.open .acc-head{color:var(--accent)}
.acc-item.open .acc-head b{color:var(--accent)}
.acc-item.open p{line-height:15.7px;padding:4px 0 14px;color:var(--body)}

.sidebar{left:597px;width:228px}
.side-list{margin-top:10px;border:1px solid var(--line);border-bottom:0}
.side-list li{height:24.5px;border-bottom:1px solid var(--line);font-size:8.6px;color:var(--muted);display:flex;align-items:center;padding-left:9px}
.side-list li::before{content:"›";margin-right:7px;color:#999}

.calendar{left:603px;top:471px;width:137px;font-size:9px;text-align:center}
.cal-head{height:20px;background:var(--cal-head);color:#fff;display:flex;align-items:center;justify-content:space-between;padding:0 5px;font-size:10.5px}
.cal-head svg{width:8px;height:10px}
.cal-days,.cal-grid{display:grid;grid-template-columns:repeat(7,1fr)}
.cal-days span{font-size:5.5px;color:#333;height:16px;line-height:16px}
.cal-grid span{height:19px;line-height:18px;background:var(--cal-cell);border:1px solid #fff;color:#333}
.cal-grid span.off{background:var(--cal-off);color:#999}
.cal-grid span.today{background:#fff;box-shadow:inset 0 0 0 1.5px var(--today)}

.site-footer{left:0;top:937px;width:885px;height:230px;background:var(--footer)}
.footer-base{left:0;top:1167px;width:885px;height:33px;background:var(--base)}
.foot-title{font:7px "Arimo",sans-serif;color:var(--footer-text);display:inline-block;padding-bottom:3px;border-bottom:1px solid var(--footer-text)}
.foot-contact{left:63px;top:965px;width:230px;font:7px/10px "Arimo",sans-serif;color:var(--footer-text)}
.foot-contact p{margin-top:10px}
.foot-contact a{color:var(--accent)}
.foot-articles{left:319px;top:965px;width:240px}
.foot-articles ul{margin-top:14px;border:1px solid var(--footer-line);border-bottom:0}
.foot-articles li{height:24.5px;border-bottom:1px solid var(--footer-line);display:flex;align-items:center;padding-left:9px;font:8px "Arimo",sans-serif;color:var(--accent)}
.foot-articles li::before{content:"›";margin-right:7px}
</style>
</head>
<body>

<div class="top-bar abs"><a href="#">Login</a></div>

<div class="brand abs">
  <span class="brand-mark"></span>
  <span class="brand-name">Center for Cellular Datacraft</span>
</div>

<nav class="main-nav abs">
  <a href="#">Home</a>
  <a href="#">Mission Statement</a>
  <a href="#">Educational Programs</a>
  <a href="#">Events</a>
  <a href="#">News</a>
  <a href="#" class="current">About Us</a>
  <a href="#">Contact</a>
</nav>

<header class="title-band abs">
  <h1>About Us 2</h1>
  <p>Who we are, what we do and why we do it.</p>
</header>

<figure class="hero abs" role="img" aria-label="Photo of a smiling staff member in blue scrubs with a stethoscope in a lab">
  <blockquote>“You could include a quote here from a staff member or a patient.”</blockquote>
  <cite>- This increases the sense of personality of the site.</cite>
</figure>

<article class="article abs">
  <p>Lorem ipsum dolor sit amet, consectetur adipiscing elit. Donec non mauris diam. Vivamus ante lorem, semper ut hendrerit nec, commodo quis lectus. Donec eu massa eu lacus rutrum adipiscing eget nec metus. Nulla eu lacus sit amet lorem rutrum imperdiet. Morbi lacus neque, feugiat laoreet elementum ut, imperdiet sed risus. Nam vulputate est id risus mattis eu consequat libero ullamcorper. Nam viverra, ante ut facilisis ullamcorper, justo enim vehicula augue, vel congue lacus diam ac lectus. Aliquam rutrum malesuada massa, id rhoncus sapien venenatis id. Praesent mauris est, tempor at luctus eu, condimentum eget arcu. Curabitur et ligula justo. In hac habitasse platea dictumst. Ut fringilla viverra erat, ut iaculis nisi interdum commodo. Vivamus interdum elementum tortor, a adipiscing magna auctor sed. Donec gravida ante at est laoreet a blandit sem rhoncus.</p>
  <p>Sed tristique tincidunt congue. Fusce condimentum scelerisque felis in imperdiet. Suspendisse potenti. Aliquam molestie egestas sapien commodo vulputate. Donec est turpis, cursus ac viverra in, mollis sit amet felis. Nullam tincidunt pulvinar mauris. Nullam vel sem sapien, id mollis velit. Integer libero ligula, hendrerit dictum luctus sit amet, cursus a neque. Proin molestie nunc vel ipsum</p>
</article>

<section class="more abs">
  <h2 class="section-title">More about us</h2>
  <div class="accordion">
    <div class="acc-item open">
      <div class="acc-head">Who we are <b>–</b></div>
      <p>Lorem ipsum dolor sit amet, consectetur adipiscing elit. Suspendisse viverra mauris eget tortor imperdiet vehicula. Proin egestas diam ac mauris molestie hendrerit. Quisque nec nisi tortor. Etiam at mauris sit amet magna suscipit hend merit non sed ligula. Vivamus purus odio.</p>
    </div>
    <div class="acc-item"><div class="acc-head">What we do <b>+</b></div></div>
    <div class="acc-item"><div class="acc-head">Why we do it <b>+</b></div></div>
    <div class="acc-item"><div class="acc-head">Where we do it <b>+</b></div></div>
  </div>
</section>

<aside class="sidebar abs" style="top:228px">
  <h2 class="section-title">Categories</h2>
  <ul class="side-list">
    <li>Design</li><li>Film</li><li>Music</li><li>Photography</li><li>Travel</li><li>TV</li><li>Uncategorized</li>
  </ul>
</aside>

<h2 class="section-title abs" style="left:604px;top:446px">Events</h2>
<div class="calendar abs">
  <div class="cal-head">
    <svg viewBox="0 0 8 10"><path d="M6 1 2 5l4 4" fill="none" stroke="#fff" stroke-width="2"/></svg>
    <span>March &nbsp;2013</span>
    <svg viewBox="0 0 8 10"><path d="M2 1l4 4-4 4" fill="none" stroke="#fff" stroke-width="2"/></svg>
  </div>
  <div class="cal-days"><span>MON</span><span>TUE</span><span>WED</span><span>THU</span><span>FRI</span><span>SAT</span><span>SUN</span></div>
  <div class="cal-grid">
    <span class="off">25</span><span class="off">26</span><span class="off">27</span><span class="off">28</span><span>1</span><span>2</span><span>3</span>
    <span>4</span><span>5</span><span>6</span><span>7</span><span>8</span><span>9</span><span>10</span>
    <span>11</span><span>12</span><span>13</span><span>14</span><span>15</span><span>16</span><span>17</span>
    <span>18</span><span>19</span><span class="today">20</span><span>21</span><span>22</span><span>23</span><span>24</span>
    <span>25</span><span>26</span><span>27</span><span>28</span><span>29</span><span>30</span><span>31</span>
    <span class="off">1</span><span class="off">2</span><span class="off">3</span><span class="off">4</span><span class="off">5</span><span class="off">6</span><span class="off">7</span>
  </div>
</div>

<aside class="sidebar abs" style="top:646px">
  <h2 class="section-title">Archives</h2>
  <ul class="side-list">
    <li>March 2013</li><li>November 2012</li><li>September 2012</li><li>July 2012</li><li>May 2012</li><li>April 2012</li><li>January 2012</li><li>August 2011</li>
  </ul>
</aside>

<footer class="site-footer abs"></footer>
<div class="foot-contact abs">
  <h3 class="foot-title">CONTACT US</h3>
  <p>Lorem ipsum dolor sit amet, consectetuer adipiscing elit. Nam cursus. Morbi ut mi. Nullam enim leo, egestas id, condimentum at, laoreet mattis, massa. Sed eleifend nonummy diam. Praesent mauris ante, elementum et, bibendum at, posuere sit amet, nibh. Duis tincidunt lectus quis dui viverra vestibulum.</p>
  <p>Insert Street address here<br>City, State<br>United States</p>
  <p>P:&nbsp; 555-014-2560<br>F:&nbsp; 555-014-2562</p>
  <p>E: <a href="#">info@cellulardatacraft.org</a></p>
</div>
<div class="foot-articles abs">
  <h3 class="foot-title">RECENT ARTICLES</h3>
  <ul>
    <li>Page Builder Post 1</li>
    <li>Standard Post No Sidebar</li>
    <li>Double Sidebar Post</li>
    <li>Gallery Post No Sidebars</li>
    <li>Left Sidebar Post</li>
  </ul>
</div>
<div class="footer-base abs"></div>

</body>
</html>
```